Sydney law firm, Prestwicks Solicitors, needs a flyer design!

We need a flyer design for our law firm which has been operating in Sydney for over 35 years. We want to send the flyer out to potential clients and also to existing clients to let them know the range of services that we provide. Our corporate colours are white, red and black and we would like these incorporated somewhat. The final design should be clean, modern and professional.

We would like the design to fit a double sided flyer approx. 210mm high x 100mm wide.

Industry/Entity Type

Law Firm

Font styles to use
Serif
Sans Serif

Colors
eb2026
ffffff

Requirements
Must have
• Details needed on the flyer are:
• Prestwicks Solicitors
• 3/82 Carradine Street, Liverpool, NSW 2170
• (02) 9418 3562
• www.prestwickssolicitors-example.com.au
• info@prestwickssolicitors-example.com.au
• Our areas of practice include:
• Property Law
• Conveyancing
• Leases
• Criminal Law
• Family Law
• Litigation and Dispute Resolution
• Company Law
• Wills and Estates
• Powers of Attorney and Guardianship
Should not have
• a picture of scales or a picture of a gavel

```html
<!DOCTYPE html>
<html lang="en">
<head>
<meta charset="utf-8">
<title>Prestwicks Solicitors Flyer</title>
<link href="https://fonts.googleapis.com/css2?family=Arimo:wght@400;700&family=Arvo:wght@700&family=Caladea&display=swap" rel="stylesheet">
<style>
  :root {
    --board: #ffffff;
    --ink: #000000;
    --paper-text: #ffffff;
    --brand-red: #eb2026;
    --label: #111111;
    --stone-light: #e6d6bd;
    --stone-mid: #c2a684;
    --stone-dark: #6e5a44;
  }
  * { margin: 0; padding: 0; box-sizing: border-box; }
  html, body { width: 1200px; height: 1000px; overflow: hidden; background: var(--board); }
  .board { position: relative; width: 1200px; height: 1000px; font-family: "Arimo", Arial, sans-serif; }
  .board-title, .view-label {
    position: absolute; text-align: center; font-weight: 400;
    font-family: "Caladea", Georgia, serif; color: var(--label);
  }
  .board-title { top: 66px; left: 0; width: 100%; font-size: 20px; }
  .view-label { top: 910px; width: 382px; font-size: 19px; }
  .view-label-front { left: 194px; }
  .view-label-back { left: 624px; }
  .flyer {
    position: absolute; top: 110px; width: 382px; height: 779px;
    background: var(--ink); color: var(--paper-text);
    box-shadow: 3px 3px 5px rgba(0,0,0,0.35);
  }
  .flyer-front { left: 194px; }
  .flyer-back { left: 624px; }
  .firm-name {
    position: absolute; top: 42px; right: 46px;
    font-family: "Arimo", Arial, sans-serif; font-weight: 400;
    font-size: 18px; line-height: 22px; color: var(--paper-text);
  }
  .hero-photo {
    position: absolute; top: 101px; left: 0; width: 382px; height: 276px;
    background: linear-gradient(100deg, var(--stone-dark) 0%, var(--stone-mid) 25%, var(--stone-light) 50%, var(--stone-mid) 75%, var(--stone-light) 100%);
  }
  .header-rule { position: absolute; top: 101px; left: 0; width: 382px; height: 1px; background: var(--brand-red); opacity: 0.7; }
  .headline {
    position: absolute; top: 406px; left: 47px;
    font-family: "Arvo", Georgia, serif; font-weight: 700; font-size: 35px; line-height: 40px;
  }
  .body-copy { position: absolute; left: 47px; font-size: 11.3px; line-height: 15.2px; }
  .body-copy p + p { margin-top: 10px; }
  .front-intro { top: 453px; }
  .back-intro { top: 136px; }
  .practice-list { position: absolute; top: 396px; left: 47px; list-style: none; font-size: 11.3px; }
  .practice-list li { position: relative; padding-left: 14px; height: 19px; line-height: 15px; }
  .practice-list li::before {
    content: ""; position: absolute; left: 0; top: 4px; width: 8px; height: 8px;
    border: 1px solid var(--brand-red);
  }
  .contact { position: absolute; top: 609px; left: 47px; font-size: 11.3px; line-height: 15.4px; font-style: normal; }
  .contact-heading { font-weight: 700; margin-bottom: 10px; }
  .contact-key { font-weight: 700; display: inline-block; width: 12px; }
  .contact-web { margin-top: 10px; color: var(--brand-red); font-weight: 700; }
</style>
</head>
<body>
<main class="board">
  <h1 class="board-title">Prestwicks Solicitors Flyer Design_03</h1>

  <section class="flyer flyer-front">
    <p class="firm-name">Prestwicks Solicitors</p>
    <div class="hero-photo" role="img" aria-label="Photograph of classical stone columns in warm sandstone light"></div>
    <h2 class="headline">Who we are</h2>
    <div class="body-copy front-intro">
      <p>Prestwicks Solicitors is a private law firm based<br>in Liverpool that has been servicing the Sydney area<br>for over 35 years. With a dedicated, professional<br>and friendly team we pride ourselves on delivering<br>an exceptional legal service to our clients.</p>
      <p>Offering a complete legal service at affordable rates,<br>our clients really do come first.</p>
    </div>
    <address class="contact">
      <p class="contact-heading">For further information, please contact:</p>
      <p>Prestwicks Solicitors<br>3/82 Carradine Street<br>Liverpool, NSW 2170<br><span class="contact-key">T</span> (02) 9418 3562<br><span class="contact-key">E</span> info@prestwickssolicitors-example.com.au</p>
      <p class="contact-web">www.prestwickssolicitors-example.com.au</p>
    </address>
  </section>

  <section class="flyer flyer-back">
    <p class="firm-name">Prestwicks Solicitors</p>
    <div class="header-rule"></div>
    <div class="body-copy back-intro">
      <p>Clients benefit from our extensive knowledge of the law,<br>vast network of professional and legal advisers as well as<br>our unmatched client service experience. We understand<br>the complex nature of the law and legal transactions<br>and strive to simplify the process for our clients. Through<br>communication, knowledge and focus we help our clients<br>understand where they want to be and how they can get<br>there. The law is constantly changing and with clients<br>ranging from individuals to large corporations we ensure<br>that our legal solutions are up-to-date and tailored to our<br>clients’ individual needs.</p>
      <p>We are passionate about our profession and committed<br>to delivering results for our clients, so no matter what your<br>legal enquiry is we are happy to listen.</p>
      <p>Our areas of practice include:</p>
    </div>
    <ul class="practice-list">
      <li>Property Law</li>
      <li>Conveyancing</li>
      <li>Leases</li>
      <li>Criminal Law</li>
      <li>Family Law</li>
      <li>Litigation and Dispute Resolution</li>
      <li>Company Law</li>
      <li>Wills and Estates</li>
      <li>Powers of Attorney and Guardianship</li>
    </ul>
    <address class="contact">
      <p class="contact-heading">For further information, please contact:</p>
      <p>Prestwicks Solicitors<br>3/82 Carradine Street<br>Liverpool, NSW 2170<br><span class="contact-key">T</span> (02) 9418 3562<br><span class="contact-key">E</span> info@prestwickssolicitors-example.com.au</p>
      <p class="contact-web">www.prestwickssolicitors-example.com.au</p>
    </address>
  </section>

  <p class="view-label view-label-front">Front view</p>
  <p class="view-label view-label-back">Reverse view</p>
</main>
</body>
</html>
```